ROAM Kelvara
Ease In, You've Arrived!
Bright & Fun-filled
Mina Pollard
PO Box 82
Mellin Bay, Tarrow Isle 2094
mina@roamkelvara.com
www.roamkelvara.com
Foot prints in sand

```html
<!DOCTYPE html>
<html lang="en">
<head>
<meta charset="utf-8">
<title>ROAM Kelvara — Stationery Set</title>
<link rel="stylesheet" href="https://fonts.googleapis.com/css2?family=Open+Sans:ital,wght@0,400;0,700;1,400&display=swap">
<style>
  :root {
    --board: #a3a3a3;
    --board-edge: #e4e4e4;
    --paper: #ffffff;
    --brand-green: #6e9a2c;
    --tagline-green: #7aa33a;
    --band-dark: #3f7a70;
    --band-light: #a9cbc2;
    --footer-text: #ffffff;
    --ink: #4a4a4a;
    --fold-line: #d6d6d6;
    --photo-sea: #2f6f78;
    --photo-sand: #c9a957;
    --photo-sky: #8fa9a2;
  }
  * { box-sizing: border-box; margin: 0; padding: 0; }
  html, body { width: 1200px; height: 667px; overflow: hidden; }
  body {
    background: var(--board-edge);
    font-family: "Open Sans", Arial, sans-serif;
    position: relative;
  }
  .board {
    position: absolute; left: 12px; top: 12px; width: 1176px; height: 643px;
    background: var(--board);
  }
  .sheet {
    position: absolute; background: var(--paper);
    box-shadow: 0 1px 3px rgba(0,0,0,.25);
  }
  .brand { text-align: center; color: var(--brand-green); }
  .brand-name {
    display: block; font-weight: 700; line-height: 1; letter-spacing: -0.3px;
  }
  .brand-tagline {
    display: block; font-style: italic; color: var(--tagline-green); margin-top: 3px;
  }
  .footer-band {
    position: absolute; left: 0; right: 0;
    background: linear-gradient(90deg, var(--band-dark) 0%, var(--band-light) 55%, var(--band-dark) 100%);
    color: var(--footer-text); text-align: center; line-height: 1.35;
  }

  /* Letterhead */
  .letterhead { left: 204px; top: 31px; width: 450px; height: 600px; }
  .letterhead .brand { position: absolute; top: 30px; left: 0; right: 0; }
  .letterhead .brand-name { font-size: 19px; }
  .letterhead .brand-tagline { font-size: 6px; }
  .letterhead .footer-band { bottom: 14px; height: 22px; font-size: 5px; padding-top: 5px; }

  /* Business cards */
  .card { left: 60px; width: 192px; height: 108px; }
  .card-front { top: 228px; }
  .card-front .brand { position: absolute; top: 10px; left: 0; right: 0; }
  .card-front .brand-name { font-size: 14px; }
  .card-front .brand-tagline { font-size: 5px; }
  .card-front .name-band {
    position: absolute; top: 64px; left: 0; right: 0; height: 11px;
    background: linear-gradient(90deg, var(--band-dark), var(--band-light));
    color: var(--footer-text); font-size: 5px; text-align: center; line-height: 11px;
  }
  .card-front .card-details {
    position: absolute; top: 82px; left: 0; right: 0;
    font-size: 4px; color: var(--ink); text-align: center; line-height: 1.5;
  }
  .card-back { top: 343px; overflow: hidden; }
  .card-photo {
    position: absolute; inset: 0;
    background:
      radial-gradient(ellipse 60% 35% at 55% 55%, var(--photo-sand), transparent 70%),
      linear-gradient(170deg, var(--photo-sky) 0%, var(--photo-sea) 55%, #1f4a50 100%);
  }
  .card-back .brand {
    position: absolute; left: 8px; bottom: 8px; text-align: left; color: #ffffff;
  }
  .card-back .brand-name { font-size: 8px; }

  /* Envelopes */
  .envelope { left: 664px; width: 500px; }
  .envelope-back { top: 31px; height: 258px; }
  .envelope-back svg { position: absolute; inset: 0; }
  .envelope-back .faint-name {
    position: absolute; top: 44px; left: 0; right: 0; text-align: center;
    font-size: 18px; font-weight: 700; color: var(--brand-green); opacity: .12;
  }
  .envelope-front { top: 343px; height: 221px; }
  .envelope-front .brand { position: absolute; top: 34px; left: 0; right: 0; }
  .envelope-front .brand-name { font-size: 17px; }
  .envelope-front .brand-tagline { font-size: 5px; }
  .envelope-front .footer-band { bottom: 10px; height: 22px; font-size: 5px; padding-top: 5px; }
</style>
</head>
<body>
<main class="board">

  <section class="sheet letterhead" aria-label="Letterhead">
    <div class="brand">
      <span class="brand-name">ROAM Kelvara</span>
      <span class="brand-tagline">Ease In, You've Arrived!</span>
    </div>
    <div class="footer-band">
      PO Box 82, Mellin Bay, Tarrow Isle 2094<br>
      Ph +64 9 555 0182 | mina@roamkelvara.com | www.roamkelvara.com
    </div>
  </section>

  <section class="sheet card card-front" aria-label="Business card front">
    <div class="brand">
      <span class="brand-name">ROAM Kelvara</span>
      <span class="brand-tagline">Ease In, You've Arrived!</span>
    </div>
    <div class="name-band">Mina Pollard</div>
    <div class="card-details">
      PO Box 82, Mellin Bay, Tarrow Isle 2094<br>
      Ph +64 9 555 0182 | mina@roamkelvara.com | www.roamkelvara.com
    </div>
  </section>

  <section class="sheet card card-back" aria-label="Business card back">
    <div class="card-photo" role="img" aria-label="Aerial photograph of an island bay with turquoise water and golden sand"></div>
    <div class="brand"><span class="brand-name">ROAM Kelvara</span></div>
  </section>

  <section class="sheet envelope envelope-back" aria-label="Envelope back">
    <svg width="500" height="258" viewBox="0 0 500 258" aria-hidden="true">
      <path d="M0 8 C150 8 198 120 250 122 C302 120 350 8 500 8" fill="none" stroke="var(--fold-line)" stroke-width="1"/>
    </svg>
    <div class="faint-name">ROAM Kelvara</div>
  </section>

  <section class="sheet envelope envelope-front" aria-label="Envelope front">
    <div class="brand">
      <span class="brand-name">ROAM Kelvara</span>
      <span class="brand-tagline">Ease In, You've Arrived!</span>
    </div>
    <div class="footer-band">
      PO Box 82, Mellin Bay, Tarrow Isle 2094<br>
      Ph +64 9 555 0182 | mina@roamkelvara.com | www.roamkelvara.com
    </div>
  </section>

</main>
</body>
</html>
```